website design for a new age Real Estate Security Business

We are launching a business in real estate which no body else is doing. We are going to use technology in terms of software and hardware to provide our services.

We are going to use Big Data, IOT etc.. for our services.

NOTE: We don't want to see Shiel or buildings etc.. that directly suggests Real estate or security on this design

Target Market(s)

India

Industry/Entity Type

Real Estate

Number of Pages Required

4 page

Font styles to use
Sans Serif
Other font styles liked:
• Use Google Fonts

Requirements
Must have
• Home Page should be trendy and colourful should give user confidence to subscribe to our service.
Nice to have
• Use Google fonts.
Should not have
• Design shouldnt have Shield or Buildings that directly suggests real estate or security.

```html
<!DOCTYPE html>
<html lang="en">
<head>
<meta charset="utf-8">
<title>Terra Vigil — Home</title>
<link rel="stylesheet" href="https://fonts.googleapis.com/css2?family=Open+Sans:wght@400;600;700;800&display=swap">
<style>
:root{
  --navy:#050f1b;
  --navy-2:#0a1c33;
  --blue:#1a8cff;
  --blue-glow:#1f6fd6;
  --green:#1fa51f;
  --orange:#ff8c00;
  --ink:#333;
  --band:#e3e3e3;
  --rule:#8a8f96;
  --white:#fff;
}
*{box-sizing:border-box;margin:0;padding:0}
html,body{width:1006px;height:1200px;overflow:hidden;background:var(--white)}
body{font-family:"Open Sans",Arial,sans-serif;color:var(--ink);position:relative}

.hero{position:absolute;left:0;top:0;width:1006px;height:634px;background:var(--navy);
  clip-path:polygon(0 0,100% 0,100% 546px,503px 634px,0 546px)}
.hero-visual{position:absolute;left:0;top:66px;width:1006px;height:568px;
  background:
    radial-gradient(ellipse 16% 20% at 44% 52%,rgba(90,170,255,.55) 0%,rgba(90,170,255,0) 100%),
    radial-gradient(ellipse 14% 18% at 60% 44%,rgba(80,160,255,.45) 0%,rgba(80,160,255,0) 100%),
    radial-gradient(ellipse 30% 34% at 50% 50%,rgba(40,130,240,.75) 0%,rgba(30,110,220,.35) 55%,rgba(20,80,180,0) 100%),
    radial-gradient(ellipse 52% 22% at 50% 80%,rgba(30,120,235,.7) 0%,rgba(20,90,200,.35) 55%,rgba(10,50,120,0) 100%),
    radial-gradient(ellipse 40% 30% at 18% 70%,rgba(25,100,210,.35) 0%,rgba(25,100,210,0) 100%),
    radial-gradient(ellipse 40% 30% at 84% 72%,rgba(25,100,210,.35) 0%,rgba(25,100,210,0) 100%),
    linear-gradient(180deg,#06121f 0%,#081a30 60%,#0a2242 100%)}
.hero-frame{position:absolute;left:0;top:0}

.site-header{position:absolute;left:0;top:0;width:1006px;height:66px}
.brand{position:absolute;left:62px;top:16px;font-size:27px;font-weight:800;letter-spacing:.5px;color:var(--blue)}
.main-nav{position:absolute;right:62px;top:27px;display:flex;gap:37px}
.main-nav a{font-size:11px;font-weight:600;color:var(--white);text-decoration:none;letter-spacing:.3px}
.main-nav a.is-active{color:var(--blue)}

.services{position:absolute;left:0;top:666px;width:1006px;text-align:center}
.section-title{font-size:20px;font-weight:700;letter-spacing:.6px;color:var(--ink)}
.step{position:absolute;top:54px;width:140px;margin-left:-70px;text-align:center}
.step-badge{width:84px;height:84px;margin:0 auto;border-radius:50%;background:#e6e6e6;display:flex;align-items:center;justify-content:center}
.step-badge span{width:76px;height:76px;border-radius:50%;background:var(--blue);display:flex;align-items:center;justify-content:center}
.step-label{margin-top:16px;font-size:16px;font-weight:700;letter-spacing:.5px;color:var(--green)}
.flow-arrow{position:absolute;top:74px}
.tagline{position:absolute;left:0;top:223px;width:1006px;font-size:13px;letter-spacing:.3px}
.btn-learn{position:absolute;left:449px;top:254px;width:109px;height:32px;background:var(--orange);color:var(--white);
  font-size:11px;font-weight:600;letter-spacing:.5px;line-height:32px;text-align:center;text-decoration:none}

.newsletter{position:absolute;left:0;top:989px;width:1006px;height:153px;background:var(--band)}
.newsletter-title{position:absolute;left:65px;top:30px;font-size:19px;font-weight:700;letter-spacing:.6px;color:#2b2b2b}
.email-field{position:absolute;left:62px;top:73px;width:354px;height:40px;border:0;background:var(--white);
  padding-left:11px;font:400 11px "Open Sans",Arial,sans-serif;color:#444}
.btn-subscribe{position:absolute;left:428px;top:73px;width:124px;height:43px;border:0;background:var(--green);
  color:var(--white);font:700 12px "Open Sans",Arial,sans-serif;letter-spacing:.8px}

.site-footer{position:absolute;left:0;top:1142px;width:1006px;height:58px;background:var(--navy)}
.social{position:absolute;left:62px;top:20px;display:flex;gap:16px}
.social span{width:17px;height:17px;border-radius:50%;background:var(--white)}

.footer-card{position:absolute;left:684px;top:1082px;width:260px;height:94px}
.footer-card svg{position:absolute;left:0;top:0}
.footer-brand{position:absolute;left:0;top:16px;width:260px;text-align:center;font-size:23px;font-weight:800;letter-spacing:.5px;color:var(--blue)}
.copyright{position:absolute;left:0;top:52px;width:260px;text-align:center;font-size:10.5px;line-height:16px;color:var(--white)}
</style>
</head>
<body>

<section class="hero">
  <div class="hero-visual" role="img" aria-label="Glowing blue 3D data landscape: a dotted terrain of connected points rising to a central peak, with thin value markers standing above it on a dark grid"></div>
  <svg class="hero-frame" width="1006" height="120" viewBox="0 0 1006 120">
    <polyline points="13,101 48,66 992,66" fill="none" stroke="var(--rule)" stroke-width="1"/>
    <circle cx="13" cy="101" r="2.5" fill="var(--white)"/>
  </svg>
</section>

<header class="site-header">
  <div class="brand">TERRA VIGIL</div>
  <nav class="main-nav">
    <a class="is-active" href="#">HOME</a>
    <a href="#">SERVICES</a>
    <a href="#">PRICING</a>
    <a href="#">CONTACT US</a>
  </nav>
</header>

<section class="services">
  <h2 class="section-title">WHAT WE DO</h2>

  <div class="step" style="left:277px">
    <div class="step-badge"><span>
      <svg width="36" height="38" viewBox="0 0 36 38" fill="var(--white)">
        <ellipse cx="18" cy="6" rx="17" ry="5.5"/>
        <path d="M1 11c0 3 7.6 5.5 17 5.5S35 14 35 11v6c0 3-7.6 5.5-17 5.5S1 20 1 17z"/>
        <path d="M1 22c0 3 7.6 5.5 17 5.5S35 25 35 22v6c0 3-7.6 5.5-17 5.5S1 31 1 28z"/>
      </svg>
    </span></div>
    <div class="step-label">DATA</div>
  </div>

  <svg class="flow-arrow" style="left:342px" width="96" height="46" viewBox="0 0 96 46" fill="none" stroke="#8e8e8e" stroke-width="2">
    <path d="M2 8c24 16 56 14 90-2"/>
    <path d="M58 3l34 3-24 38"/>
  </svg>

  <div class="step" style="left:503px">
    <div class="step-badge"><span>
      <svg width="46" height="36" viewBox="0 0 46 36" fill="none" stroke="var(--white)" stroke-width="3.5">
        <path d="M2 2v32h42"/>
        <path d="M9 27l10-11 7 6 12-13" stroke-linejoin="round"/>
        <path d="M31 7h8v8" fill="var(--white)" stroke-width="2"/>
      </svg>
    </span></div>
    <div class="step-label">ANALYSIS</div>
  </div>

  <svg class="flow-arrow" style="left:568px" width="98" height="46" viewBox="0 0 98 46" fill="none" stroke="#8e8e8e" stroke-width="2">
    <path d="M2 36c28-20 60-16 92-12"/>
    <path d="M66 2l28 22-34 6"/>
  </svg>

  <div class="step" style="left:730px">
    <div class="step-badge"><span>
      <svg width="44" height="40" viewBox="0 0 44 40" fill="var(--white)">
        <g transform="translate(14 22)">
          <rect x="-3" y="-13" width="6" height="26"/>
          <rect x="-3" y="-13" width="6" height="26" transform="rotate(45)"/>
          <rect x="-3" y="-13" width="6" height="26" transform="rotate(90)"/>
          <rect x="-3" y="-13" width="6" height="26" transform="rotate(135)"/>
          <circle r="9.5"/>
          <circle r="4" fill="var(--blue)"/>
        </g>
        <g transform="translate(34 10)">
          <rect x="-2" y="-8.5" width="4" height="17"/>
          <rect x="-2" y="-8.5" width="4" height="17" transform="rotate(60)"/>
          <rect x="-2" y="-8.5" width="4" height="17" transform="rotate(120)"/>
          <circle r="6"/>
          <circle r="2.5" fill="var(--blue)"/>
        </g>
        <g transform="translate(34 30)">
          <rect x="-2" y="-8.5" width="4" height="17"/>
          <rect x="-2" y="-8.5" width="4" height="17" transform="rotate(60)"/>
          <rect x="-2" y="-8.5" width="4" height="17" transform="rotate(120)"/>
          <circle r="6"/>
          <circle r="2.5" fill="var(--blue)"/>
        </g>
      </svg>
    </span></div>
    <div class="step-label">ACTION</div>
  </div>

  <p class="tagline">To keep your property Safe</p>
  <a class="btn-learn" href="#">LEARN MORE</a>
</section>

<section class="newsletter">
  <h2 class="newsletter-title">NEWSLETTER SUBSCRIBE</h2>
  <input class="email-field" type="email" placeholder="Enter Email Address" aria-label="Email address">
  <button class="btn-subscribe" type="button">SUBSCRIBE</button>
</section>

<footer class="site-footer">
  <div class="social" aria-label="Social links">
    <span role="img" aria-label="Social network 1"></span>
    <span role="img" aria-label="Social network 2"></span>
    <span role="img" aria-label="Social network 3"></span>
    <span role="img" aria-label="Social network 4"></span>
    <span role="img" aria-label="Social network 5"></span>
  </div>
</footer>

<div class="footer-card">
  <svg width="260" height="94" viewBox="0 0 260 94">
    <polygon points="22,1 259,1 259,64 229,93 1,93 1,22" fill="var(--navy)" stroke="var(--rule)" stroke-width="1.5"/>
  </svg>
  <div class="footer-brand">TERRA VIGIL</div>
  <p class="copyright">Copyright © 2017. Company Name.<br>All Right Reserved</p>
</div>

</body>
</html>
```